KRTLO Promotion Flyer to raise money and communicate our goals

We need a flyer that promotes our organization. We are a 501(c)3 trying to raise money for Arts, Education and Entrepreneurship in our small town.

We promote a social events that improve qualtiy of life and educate people on how to start and expand businesses. Our goal is to make downtown an active and thriving place with many things for people to do and enjoy as well as create a favorable place for business.

Target Market(s)

Wealthy donors and Organizations with cash

Industry/Entity Type

Education

Colors

Designer to choose colors to be used in the design.

Requirements
Must have
• Eye catching graphics and look very professional
• Should appeal to men and women
Nice to have
• Make use of any known psychological colors and fonts etc... that appeal to philanthropic people
Should not have
• Should not be complicated or confusing

```html
<!DOCTYPE html>
<html lang="en">
<head>
<meta charset="utf-8">
<title>KRTLO Membership Flyer</title>
<link rel="stylesheet" href="https://fonts.googleapis.com/css2?family=Roboto+Condensed:wght@400;700&display=swap">
<style>
  :root {
    --paper: #f7f7f9;
    --ink: #2e2e33;
    --magenta: #e5197a;
    --band-blue: #0d87c9;
    --sky-blue: #1aa3e0;
    --leaf-green: #7cbc3f;
    --ring-grey: #c9c9cf;
    --white: #ffffff;
    --violet: #7a5fb0;
  }
  * { box-sizing: border-box; margin: 0; padding: 0; }
  html, body { width: 846px; height: 1200px; overflow: hidden; background: var(--paper); }
  body { font-family: "Roboto Condensed", "Arial Narrow", sans-serif; color: var(--ink); }
  .flyer { position: relative; width: 846px; height: 1200px; overflow: hidden; background: var(--paper); }
  .header-art { position: absolute; left: 0; top: 0; width: 846px; height: 520px; }
  .emblem {
    position: absolute; left: 72px; top: 122px; width: 236px; height: 236px;
    border-radius: 50%; background: var(--white); border: 1px solid var(--ring-grey);
    display: flex; align-items: center; justify-content: center; gap: 10px;
  }
  .emblem-dot { width: 18px; height: 18px; border-radius: 50%; background: var(--magenta); }
  .emblem-name { font-size: 44px; font-weight: 700; color: var(--magenta); letter-spacing: 1px; }
  .intro {
    position: absolute; left: 79px; top: 424px; width: 680px;
    font-size: 17px; line-height: 22px; color: var(--ink);
  }
  .intro strong { color: var(--magenta); font-weight: 700; }
  .mission-band {
    position: absolute; left: 0; top: 589px; width: 846px; height: 296px;
    background: var(--band-blue); padding: 18px 0 0 0;
  }
  .mission-item { display: flex; align-items: flex-start; height: 66px; padding-left: 84px; }
  .mission-icon {
    flex: none; width: 56px; height: 56px; border-radius: 50%; background: var(--white);
    display: flex; align-items: center; justify-content: center; margin-top: 0;
  }
  .mission-text {
    margin-left: 30px; width: 600px; color: var(--white);
    font-size: 17px; line-height: 21px; padding-top: 4px;
  }
  .mission-text strong { font-weight: 700; }
  .appeal {
    position: absolute; left: 88px; top: 912px; width: 680px;
    column-count: 2; column-gap: 42px;
    font-size: 15.5px; line-height: 20.5px; color: var(--ink);
  }
  .skyline { position: absolute; left: 0; top: 1100px; width: 846px; height: 100px; }
  .corner-mark { position: absolute; }
</style>
</head>
<body>
<main class="flyer">

  <svg class="header-art" viewBox="0 0 846 520" aria-hidden="false">
    <defs>
      <linearGradient id="photoTone" x1="0" y1="0" x2="0" y2="1">
        <stop offset="0" stop-color="#dfe7ee"/>
        <stop offset="0.38" stop-color="#cdbf9f"/>
        <stop offset="0.55" stop-color="#5e8a3c"/>
        <stop offset="1" stop-color="#4f7d2e"/>
      </linearGradient>
      <linearGradient id="swooshBlue" x1="0" y1="0" x2="0" y2="1">
        <stop offset="0" stop-color="#1aa3e0"/>
        <stop offset="1" stop-color="#8fd3f4"/>
      </linearGradient>
    </defs>
    <path role="img" aria-label="Photo of the town event hall with a white gazebo on a green lawn"
          d="M205,0 L846,0 L846,472 C760,492 650,496 560,470 C420,400 265,210 205,0 Z"
          fill="url(#photoTone)"/>
    <path class="bottom-swoosh" d="M470,455 C600,505 740,505 846,470 L846,490 C730,522 600,515 470,455 Z" fill="var(--sky-blue)"/>
    <path class="magenta-swoosh" d="M178,0 L214,0 C270,210 420,380 590,484 C400,400 240,220 178,0 Z" fill="var(--magenta)"/>
    <path class="blue-swoosh" d="M134,0 L152,0 C160,60 175,110 198,150 C165,110 142,60 134,0 Z" fill="url(#swooshBlue)"/>
    <path class="ring-arc-blue" d="M100,175 A120,120 0 0 1 175,120" fill="none" stroke="var(--sky-blue)" stroke-width="3"/>
    <path class="ring-arc-green" d="M80,300 A124,124 0 0 0 300,300" fill="none" stroke="var(--leaf-green)" stroke-width="3"/>
    <polygon class="corner-triangle" points="50,46 92,46 71,80" fill="#8a7cc0"/>
  </svg>

  <div class="emblem">
    <span class="emblem-dot"></span>
    <span class="emblem-name">KRTLO</span>
  </div>

  <p class="intro">
    The <strong>Kerrington Small Business Association</strong><br>
    <strong>(KRTLO)</strong> is a local leader in the areas of Arts, Education<br>
    and Entrepreneurship and is working diligently to promote<br>
    Kerrington and revitalize our downtown. When you become an<br>
    KRTLO Member, you will be a part of the citywide work that the KRTLO does every day<br>
    to improve the lives of citizens of Kerrington:
  </p>

  <section class="mission-band">
    <div class="mission-item">
      <span class="mission-icon">
        <svg width="30" height="30" viewBox="0 0 30 30" fill="none" stroke="var(--magenta)" stroke-width="2.2" stroke-linejoin="round">
          <path d="M4,12 L10,12 L22,5 L22,25 L10,18 L4,18 Z"/><path d="M8,18 L10,26 L14,26 L12,18"/>
        </svg>
      </span>
      <p class="mission-text"><strong>We promote:</strong> Kerrington Hotels, Shopping and Events that make Kerrington a pleasant, exciting and prosperous place to live.</p>
    </div>
    <div class="mission-item">
      <span class="mission-icon">
        <svg width="32" height="32" viewBox="0 0 32 32" fill="var(--magenta)">
          <rect x="13" y="4" width="16" height="12" fill="none" stroke="var(--magenta)" stroke-width="2"/>
          <circle cx="8" cy="7" r="3"/><rect x="5" y="11" width="6" height="9" rx="1"/>
          <circle cx="7" cy="23" r="2.5"/><circle cx="16" cy="23" r="2.5"/><circle cx="25" cy="23" r="2.5"/>
          <rect x="4" y="26" width="6" height="5" rx="1"/><rect x="13" y="26" width="6" height="5" rx="1"/><rect x="22" y="26" width="6" height="5" rx="1"/>
        </svg>
      </span>
      <p class="mission-text"><strong>We provide:</strong> training and resources to anyone interested Arts, Education and Entrepreneurship.</p>
    </div>
    <div class="mission-item">
      <span class="mission-icon">
        <svg width="30" height="30" viewBox="0 0 30 30" fill="var(--magenta)">
          <circle cx="15" cy="9" r="6"/><path d="M4,29 C4,20 9,17 15,17 C21,17 26,20 26,29 Z"/>
        </svg>
      </span>
      <p class="mission-text"><strong>We help:</strong> entrepreneur's start and grow their businesses in a tax efficient and appropriate way.</p>
    </div>
    <div class="mission-item">
      <span class="mission-icon">
        <svg width="32" height="32" viewBox="0 0 32 32" fill="var(--magenta)">
          <circle cx="16" cy="16" r="8" fill="none" stroke="var(--magenta)" stroke-width="2"/>
          <circle cx="16" cy="5" r="3.5"/><circle cx="26" cy="12" r="3.5"/><circle cx="22" cy="25" r="3.5"/>
          <circle cx="10" cy="25" r="3.5"/><circle cx="6" cy="12" r="3.5"/>
        </svg>
      </span>
      <p class="mission-text"><strong>We work</strong> with all levels of local government to promote our community and create a fertile environment for growth.</p>
    </div>
  </section>

  <p class="appeal">
    Every day, we look for ways to help our local businesses grow and expand, but we need you by our side. As an KRTLO Member, you can help provide training, education and support, and you can give our many businesses a chance to grow and our citizens the opportunity to experience big town amenities and events in a small town. Members' regular monthly gifts provide a consistent, reliable income stream that allows us to spend less time fundraising—and more time helping our businesses and community. Becoming an KRTLO Member is an easy, efficient and tax–deductible way to make a difference for our community all year long. Please donate today.
  </p>

  <svg class="skyline" viewBox="0 0 846 100">
    <defs>
      <linearGradient id="skylineTone" x1="0" y1="0" x2="1" y2="0">
        <stop offset="0" stop-color="#1a6fd0"/>
        <stop offset="0.5" stop-color="#6a3fb8"/>
        <stop offset="1" stop-color="#e5197a"/>
      </linearGradient>
    </defs>
    <rect role="img" aria-label="Illustrated city skyline in blue, violet and magenta tones"
          x="90" y="20" width="700" height="80" fill="url(#skylineTone)"/>
    <polygon class="corner-triangle" points="735,4 775,4 755,38" fill="#f29cc6"/>
  </svg>

</main>
</body>
</html>
```